The Pick of Lorne - Album

Hi all

I am planning on releasing my first album for online distribution shortly. I have chosen the tracks that I want to put in it. You can listen to them through my set "The Pick of Lorne": http://tunevault.example/halwickl/sets/the-pick-of-lorne

I am not particularly happy with the name "The Pick Of Lorne", so I have created a competition to find a better album name. Anyone is welcome to enter. The best two entries will win a free copy of the album when it comes out:
http://tunevault.example/halwickl/album-name
The album name competition will end on December 17.
If you have a design idea before that time, feel free to submit that as well as the album name. You can send as many ideas as you like.
After the album name is decided upon, this will be like a normal design competition.
I am planning on distributing the album online through VestaDisc.
According to vestadisc.example: "Submitted cover art must be 1500 x 1500 pixels jpg. It cannot be blurry or pixilated and must be perfectly square."
The artwork should probably contain something like "by Lorne Halwick" as well as the title.
VestaDisc make choose to make a CD version of the album, but I believe they use the .jpg file to generate that.

Thanks in advance,
Lorne :)
Updates

A mosaic, patchwork or collage would be good, to reflect the variety of the music.

I have added a couple of photos that you may or may not want to use. One is of me, the other is of my "studio", most of which is my laptop. :)

I hope that helps. (now you know why I haven't included these already)

Hi everyone

Thanks to all those who entered.

I received many suggestions, and the decision was tough.

Eventually I decided on "Tivet Brassel" as the name.
It is the name of one of the pieces on the album: http://tunevault.example/halwickl/tivetbrassel

Hopefully this will draw in the audience that will appreciate my quirky music.

The runners up were "The Echoes Of" and "A Far Shore". Both of these two were submitted by Sketch Harbor participants.
I will organise a copy of the album to be sent to those people once the album comes out.

For background, the "Modal" part of the name was from the musical concept of a mode, being an arrangement of a series of notes (scale). "Podal" was my way of expressing a dismissive attitude to that - sort of like "Who needs conventional music theory".

Thanks again,
and good luck with the designs,
Lorne :)

Target Market(s)

People who buy music online. My music covers a wide range.

Industry/Entity Type

Online

```html
<!DOCTYPE html>
<html lang="en">
<head>
<meta charset="utf-8">
<title>Tivet Brassel — by Lorne Halwick</title>
<link rel="stylesheet" href="https://fonts.googleapis.com/css2?family=Bungee&family=Cormorant+Garamond:ital,wght@1,600&display=swap">
<style>
  :root {
    --paper: #ffffff;
    --teal-light: #a9dde2;
    --teal: #3fb6c4;
    --teal-deep: #1f7f92;
    --crimson: #7a0d06;
    --crimson-deep: #3a0703;
    --gold: #f7b21b;
    --byline: #ffffff;
  }
  html, body {
    margin: 0;
    padding: 0;
    overflow: hidden;
    background: var(--paper);
  }
  .cover {
    position: relative;
    width: 1200px;
    height: 1200px;
    background: var(--paper);
    overflow: hidden;
  }
  .band {
    position: absolute;
    left: 46px;
    width: 1088px;
    z-index: 1;
  }
  .band--one {
    top: 44px; height: 232px;
    background: linear-gradient(90deg, var(--paper) 0%, var(--teal-light) 14%, var(--teal) 35%, var(--teal-deep) 58%, var(--crimson) 62%, var(--crimson-deep) 100%);
  }
  .band--two {
    top: 304px; height: 232px;
    background: linear-gradient(90deg, var(--crimson-deep) 0%, var(--crimson) 30%, #5a1208 48%, var(--teal-deep) 54%, var(--teal) 68%, var(--teal-light) 86%, var(--paper) 100%);
  }
  .band--three {
    top: 656px; height: 230px;
    background: linear-gradient(90deg, var(--teal-light) 0%, var(--teal) 25%, var(--teal-deep) 50%, var(--crimson) 56%, var(--crimson-deep) 100%);
  }
  .band--four {
    top: 914px; height: 220px;
    background: linear-gradient(90deg, var(--crimson-deep) 0%, var(--crimson) 18%, var(--teal-deep) 30%, var(--teal) 48%, var(--teal-light) 100%);
  }
  .title {
    position: absolute;
    left: 90px;
    top: 540px;
    width: 1030px;
    height: 112px;
    margin: 0;
    z-index: 2;
  }
  .title svg {
    display: block;
  }
  .title text {
    font-family: "Bungee", sans-serif;
    font-size: 92px;
    fill: var(--gold);
  }
  .byline {
    position: absolute;
    right: 84px;
    top: 652px;
    margin: 0;
    z-index: 3;
    white-space: nowrap;
    font-family: "Cormorant Garamond", serif;
    font-style: italic;
    font-weight: 600;
    font-size: 40px;
    line-height: 1.2;
    color: var(--byline);
  }
</style>
</head>
<body>
  <main class="cover">
    <div class="band band--one" role="img" aria-label="Painted profile of a red face meeting turquoise brushwork"></div>
    <div class="band band--two" role="img" aria-label="Painted red profile facing right into turquoise haze"></div>
    <h1 class="title">
      <svg width="1030" height="112" viewBox="0 0 1030 112" aria-label="Tivet Brassel">
        <text x="0" y="96" textLength="1030" lengthAdjust="spacing">TIVET BRASSEL</text>
      </svg>
    </h1>
    <div class="band band--three" role="img" aria-label="Turquoise brushwork meeting a red painted profile"></div>
    <div class="band band--four" role="img" aria-label="Red painted profile on the left of a wide turquoise field"></div>
    <p class="byline">by lorne Halwick</p>
  </main>
</body>
</html>
```